Logo and Double sided business card

We need a logo and business card for a Point of Sale Business, Website is www.kestreltill.com.au - this is being worked on at the moment. There is a logo on the website - but this is more of a placement /logo and needs to be redesigned.
The address for Details for the Business card are

Person Name
KESTREL TILL
17/3 Worrigal Pde
Marlow Vale 2671
Ph 1300 585 926 (1300 KTL 926)
Email : Person@kestreltill.com.au
Web: www.kestreltill.com.au

Our company will be a Point of Sale installation and Support business. We Specialise in the Vandrel Quill system.

We do
Installation of POS Systems
Support and Maintenance of existing POS
Quill POS support
Updates

Target Market(s)

Restaurants, hotels, retail shops

Industry/Entity Type

Business

Contact Information for Business Card

Person Name
KESTREL TILL
17/3 Worrigal Pde
Marlow Vale 2671
Web: www.kestreltill.com.au

Logo Text

Kestrel Till

Font styles to use
Serif

Requirements
Must have
• We must have the source graphics in editable formats for both logo and business card.

```html
<!DOCTYPE html>
<html lang="en">
<head>
<meta charset="utf-8">
<title>Kestrel Till — Business Card</title>
<link rel="stylesheet" href="https://fonts.googleapis.com/css2?family=Noto+Serif:wght@400;700&display=swap">
<style>
  :root {
    --backdrop: #e4e4e4;
    --card: #ffffff;
    --brand-orange: #d98300;
    --ink: #3a3a3a;
    --ghost: #f1f1f1;
  }
  * { margin: 0; padding: 0; box-sizing: border-box; }
  html, body {
    width: 1200px;
    height: 900px;
    overflow: hidden;
    background: var(--backdrop);
  }
  .sheet {
    width: 1200px;
    height: 900px;
    display: flex;
    align-items: center;
    justify-content: center;
    gap: 60px;
  }
  .card {
    position: relative;
    width: 520px;
    height: 297px;
    background: var(--card);
    box-shadow: 0 6px 18px rgba(0,0,0,0.12);
    overflow: hidden;
    font-family: "Noto Serif", serif;
  }
  /* front */
  .card-front {
    display: flex;
    flex-direction: column;
    align-items: center;
    justify-content: center;
    gap: 18px;
  }
  .brand-dot {
    width: 92px;
    height: 92px;
    border-radius: 50%;
    background: var(--brand-orange);
  }
  .brand-name {
    color: var(--brand-orange);
    font-weight: 700;
    font-size: 40px;
    line-height: 1;
    white-space: nowrap;
  }
  /* back */
  .ghost-circle {
    position: absolute;
    right: -60px;
    top: -80px;
    width: 300px;
    height: 300px;
    border-radius: 50%;
    background: var(--ghost);
  }
  .back-brand {
    position: absolute;
    right: 34px;
    top: 36px;
    display: flex;
    flex-direction: column;
    align-items: center;
    gap: 8px;
  }
  .back-brand .brand-dot { width: 40px; height: 40px; }
  .back-brand .brand-name { font-size: 18px; }
  .contact {
    position: absolute;
    left: 36px;
    top: 122px;
    list-style: none;
    color: var(--ink);
    font-size: 15px;
    line-height: 1.5;
    white-space: nowrap;
  }
</style>
</head>
<body>
  <main class="sheet">
    <section class="card card-front" aria-label="Business card front">
      <span class="brand-dot" aria-hidden="true"></span>
      <span class="brand-name">Kestrel Till</span>
    </section>

    <section class="card card-back" aria-label="Business card back">
      <span class="ghost-circle" aria-hidden="true"></span>
      <div class="back-brand">
        <span class="brand-dot" aria-hidden="true"></span>
        <span class="brand-name">Kestrel Till</span>
      </div>
      <ul class="contact">
        <li>Ph: 1300 585 926 (1300 KTL 926)</li>
        <li>Person@kestreltill.com.au</li>
        <li>www.kestreltill.com.au</li>
        <li>17/3 Worrigal Pde,</li>
        <li>Marlow Vale - 2671</li>
      </ul>
    </section>
  </main>
</body>
</html>
```